Tin Lantern "Cold Harbor" New Single Cover

Create cover artwork for the band Tin Lantern' new single "Cold Harbor" being released early 2020. Style, font and graphics to be consistent with band's previous releases and overall brand identity. Visit www.tinlanternband.example and our Spotify page https://listen.tunevault.example/artist/8QXzrT4LmNbW2cPd7KeYjA?si=HVkR3sTpZ9wLqYb2nMcXuE to view our previous releases and overall brand identity. Some examples attached as well. We are looking for someone to work with on future projects as well.

Lyrics are here: https://pages.draftbox.example/document/d/7KpRw2mXn_9LqTe4Zs8Vd_HyjB2cF5t03Qa71nRkwLpY/edit

Music is here: https://wavecrate.example/tinlantern/cold-harbor/s-rbmtx

Font styles to use
Sans Serif

Colors

Designer to choose colors to be used in the design.

Requirements
Must have
• Must be consistent with current brand identity and with prior album / single art.

```html
<!DOCTYPE html>
<html lang="en">
<head>
<meta charset="UTF-8">
<title>Tin Lantern – Cold Harbor – Single Cover</title>
<link rel="stylesheet" href="https://fonts.googleapis.com/css2?family=Jost:wght@300;400;500&display=swap">
<style>
  :root {
    --sky: #03BEFC;
    --sky-deep: #2E9BE0;
    --violet: #7D62B8;
    --magenta: #C53290;
    --rose: #F20C70;
    --hot-pink: #FF0066;
    --frame: #FFFFFF;
    --title: #FFF200;
    --band: #1E2A4F;
  }
  html, body {
    margin: 0;
    padding: 0;
    width: 1200px;
    height: 1200px;
    overflow: hidden;
  }
  .cover {
    position: relative;
    width: 1200px;
    height: 1200px;
    background: linear-gradient(180deg,
      var(--sky) 0%,
      var(--sky) 14%,
      var(--sky-deep) 33%,
      var(--violet) 46%,
      var(--magenta) 60%,
      var(--rose) 76%,
      var(--hot-pink) 100%);
    font-family: "Jost", sans-serif;
    overflow: hidden;
  }
  .cover__frame {
    position: absolute;
    left: 36px;
    top: 44px;
    right: 38px;
    bottom: 44px;
    border: 4px solid var(--frame);
  }
  .cover__rule {
    position: absolute;
    left: 383px;
    width: 435px;
    height: 3px;
    background: var(--frame);
  }
  .cover__rule--top { top: 229px; }
  .cover__rule--bottom { top: 834px; }
  .cover__title {
    position: absolute;
    left: 0;
    right: 0;
    top: 300px;
    margin: 0;
    text-align: center;
    color: var(--title);
    font-weight: 300;
    font-size: 228px;
    line-height: 230px;
    text-transform: uppercase;
  }
  .cover__title-line { display: block; }
  .cover__title-line--first { letter-spacing: 0.22em; margin-right: -0.22em; }
  .cover__title-line--second { letter-spacing: 0.1em; margin-right: -0.1em; font-size: 200px; }
  .cover__band {
    position: absolute;
    left: 0;
    right: 0;
    top: 892px;
    margin: 0;
    text-align: center;
    color: var(--band);
    font-weight: 400;
    font-size: 98px;
    line-height: 98px;
    letter-spacing: 0.04em;
    text-transform: uppercase;
  }
  .cover__band-line { display: block; }
</style>
</head>
<body>
  <main class="cover">
    <div class="cover__frame"></div>
    <div class="cover__rule cover__rule--top"></div>
    <h1 class="cover__title">
      <span class="cover__title-line cover__title-line--first">Cold</span>
      <span class="cover__title-line cover__title-line--second">Harbor</span>
    </h1>
    <div class="cover__rule cover__rule--bottom"></div>
    <p class="cover__band">
      <span class="cover__band-line">Tin</span>
      <span class="cover__band-line">Lantern</span>
    </p>
  </main>
</body>
</html>
```